arts & crafts

I collect old plates & make them into serving plates for cakes, afternoon teas, special occasions, weddings, parties, bridal showers. cake competitions, displays in bakeries.

Contact Information for Business Card

Willow Lane Plates
Giving vintage a second life
Ph 0417283956
info@ willowlaneplates.com.au
www.willowlaneplates.com.au
pagebook
Craftlo

```html
<!DOCTYPE html>
<html lang="en">
<head>
<meta charset="utf-8">
<title>Willow Lane Plates – Business Card</title>
<link rel="stylesheet" href="https://fonts.googleapis.com/css2?family=Crimson+Text:wght@400;700&family=Dancing+Script:wght@400&display=swap">
<style>
  :root {
    --backdrop: #e9e4de;
    --card-pink: #f6bccb;
    --ink-maroon: #5a1f24;
    --ink-slate: #3b4a5a;
    --photo-deep: #1d3a2c;
    --photo-mid: #5f8a78;
    --photo-light: #dfe8e2;
  }
  * { box-sizing: border-box; margin: 0; padding: 0; }
  html, body {
    width: 1200px;
    height: 900px;
    overflow: hidden;
    background: var(--backdrop);
  }
  .canvas {
    width: 1200px;
    height: 900px;
    display: flex;
    align-items: center;
    justify-content: center;
  }
  .business-card {
    position: relative;
    width: 860px;
    height: 540px;
    display: flex;
    flex-direction: column;
    box-shadow: 0 10px 30px rgba(0,0,0,0.18);
    overflow: hidden;
  }
  .photo-panel {
    position: relative;
    height: 330px;
  }
  .photo-placeholder {
    position: absolute;
    inset: 0;
    background:
      radial-gradient(ellipse 35% 55% at 45% 45%, var(--photo-light) 0%, rgba(223,232,226,0) 70%),
      linear-gradient(150deg, var(--photo-deep) 0%, var(--photo-mid) 40%, var(--photo-light) 80%, #eef2ef 100%);
  }
  .photo-fade {
    position: absolute;
    inset: 0;
    background: linear-gradient(270deg, rgba(240,244,240,0.9) 0%, rgba(240,244,240,0) 35%);
  }
  .brand-mark {
    position: absolute;
    right: 30px;
    bottom: 14px;
    writing-mode: vertical-rl;
    transform: rotate(180deg);
    font-family: "Crimson Text", Georgia, serif;
    font-weight: 400;
    font-size: 38px;
    line-height: 1;
    white-space: nowrap;
    color: var(--ink-maroon);
  }
  .contact-panel {
    flex: 1;
    background: var(--card-pink);
    display: flex;
    flex-direction: column;
    align-items: center;
    justify-content: center;
    text-align: center;
    font-family: "Crimson Text", Georgia, serif;
  }
  .business-name {
    font-weight: 700;
    font-size: 24px;
    line-height: 1.1;
    color: var(--ink-slate);
  }
  .tagline {
    font-family: "Dancing Script", cursive;
    font-size: 19px;
    line-height: 1.2;
    color: var(--ink-slate);
    margin-bottom: 12px;
  }
  .contact-list {
    list-style: none;
    font-size: 17px;
    line-height: 1.3;
    color: var(--ink-maroon);
  }
  .contact-list .phone { margin-bottom: 8px; }
</style>
</head>
<body>
  <main class="canvas">
    <article class="business-card">
      <section class="photo-panel">
        <div class="photo-placeholder" role="img" aria-label="Soft-toned portrait photograph of a woman on grass"></div>
        <div class="photo-fade"></div>
        <p class="brand-mark">Willow Lane Plates</p>
      </section>
      <section class="contact-panel">
        <h1 class="business-name">Willow Lane Plates</h1>
        <p class="tagline">Giving vintage a second life</p>
        <ul class="contact-list">
          <li class="phone">Ph. 0417283956</li>
          <li>E: info@ willowlaneplates.com.au</li>
          <li>W: www.willowlaneplates.com.au</li>
          <li>pagebook :Craftlo</li>
        </ul>
      </section>
    </article>
  </main>
</body>
</html>
```